Ferncrest Dental, LLC business card project

Business card to be designed with current logo.
Dental office- please keep design of card that looks clean and professional.
Please include the following info:
Ferncrest Dental, LLC
Dr. Lorna Pettigrew
2871 Marlowe Street
Bethlehem, PA 18093
610-555-0193
ferncrestdental.office@examplemail.test
Hello everyone-
Reason: Just got back from overseas- will look at all designs and provide feedback. Thank you!
Reason: Polling my friends for the final selection-
thank you to all those that participated- so many talented designers!

```html
<!DOCTYPE html>
<html lang="en">
<head>
<meta charset="utf-8">
<title>Ferncrest Dental, LLC – Business Card</title>
<link rel="stylesheet" href="https://fonts.googleapis.com/css2?family=Quicksand:wght@400;500;700&display=swap">
<style>
  :root {
    --page-bg: #e4e4e4;
    --card-border: #ffffff;
    --green-deep: #5b9a4d;
    --green-light: #82b873;
    --band-dark: rgba(40, 80, 35, 0.28);
    --band-mid: rgba(40, 80, 35, 0.14);
    --band-light: rgba(255, 255, 255, 0.10);
    --ink: #ffffff;
  }
  html, body {
    margin: 0;
    width: 1200px;
    height: 861px;
    overflow: hidden;
    background: var(--page-bg);
  }
  .card {
    position: absolute;
    left: 240px;
    top: 225px;
    width: 720px;
    height: 410px;
    box-sizing: border-box;
    padding: 16px;
    background: var(--card-border);
    box-shadow: 0 10px 30px rgba(0, 0, 0, 0.18);
  }
  .card-face {
    position: relative;
    width: 100%;
    height: 100%;
    background: linear-gradient(115deg, var(--green-deep) 0%, var(--green-deep) 45%, var(--green-light) 100%);
    font-family: "Quicksand", sans-serif;
    color: var(--ink);
    overflow: hidden;
  }
  .brand {
    position: absolute;
    top: 52px;
    left: 0;
    right: 0;
    display: flex;
    justify-content: center;
    align-items: center;
    gap: 16px;
  }
  .brand-dot {
    width: 34px;
    height: 34px;
    border-radius: 50%;
    background: var(--ink);
  }
  .brand-name {
    font-size: 40px;
    font-weight: 500;
    letter-spacing: 0.5px;
  }
  .doctor-name {
    position: absolute;
    top: 158px;
    left: 0;
    right: 0;
    text-align: center;
    font-size: 30px;
    font-weight: 700;
    letter-spacing: 0.5px;
  }
  .contact-bands {
    position: absolute;
    left: 0;
    right: 0;
    bottom: 0;
    top: 222px;
    display: flex;
    flex-direction: column;
  }
  .contact-band {
    flex: 1;
    display: flex;
    align-items: center;
    justify-content: center;
    font-size: 16px;
    font-weight: 500;
    letter-spacing: 0.4px;
  }
  .contact-band--address { background: var(--band-dark); }
  .contact-band--phone { background: var(--band-mid); }
  .contact-band--email { background: var(--band-light); }
</style>
</head>
<body>
  <div class="card">
    <div class="card-face">
      <div class="brand">
        <span class="brand-dot" aria-hidden="true"></span>
        <span class="brand-name">Ferncrest Dental, LLC</span>
      </div>
      <div class="doctor-name">Dr. Lorna Pettigrew</div>
      <div class="contact-bands">
        <div class="contact-band contact-band--address">2871 Marlowe Street Bethlehem, PA 18093</div>
        <div class="contact-band contact-band--phone">610-555-0193</div>
        <div class="contact-band contact-band--email">ferncrestdental.office@examplemail.test</div>
      </div>
    </div>
  </div>
</body>
</html>
```